Inside sleeve of CD

I currently have a CD cover front and back but now need to work on the inside sleeve.
I have a series of photos to use and lyrics so its should be fairly simple.
The inside sleeve must match the theme of the cover.
We would be working on pages 2-12 ( as page 1 is the front cover).
I would like to give the brief for each page one at a time to avoid confusion however in this case I have provided 2. The size of the insert will be standard CD cover size and will be like a booklet.
Page 2:
This is a pure white background font as per the front cover
The Lyrics for two songs will be on this page running adjacent to each other, the writing will be the same orange as the album cover (song 1 and 2).
On the bottom left will be an orange cocktail umbrella resting on its side.
On the bottom right will be an instamatic photo with tape on its corners (ON AN ANGLE)- I will provide a photo of a sunrise to insert into this photo
Page 3: Palm photo provided all on its own
Page 4- Photo of truck with palm tree
Place an instamatic photo on an angle in the top left covering a corner of the truck- (photo to be provided to insert- insert image 3385.)
Place lyrics for song 3- (Quiet Harbor) on the back of the truck like its written on the truck itself- use an orange black or blue font ( whatever works)
Page 5- Song 4 and 5 are on this one. Again each song adjacent to each other- one on the right side and one on the left- lyric font in orange.
The entire background is white like page 2.
Place two instamatic photos on bottom left and right on angles ( will provide photos for these to insert into frames- image 3734 on the left and image 3386 on the right)
Page 6- Songs 6 and 7
I have provided a photo of a shadow of two people image 3402. Please put the lyrics for song 6 superimposed over the shadow on the left and put the lyrics for song 7 into the shadow of the person on the right. The lyrics will have to be staggerd to fit in each shadow- be creative and have some fun with this one.
Page 7- Songs 8 ( fold the map) and song 9 (Copper kites)
I would like a strip of 35mm film across the page (see example)
On the top left I would like song 8- you can be creative here if you like.
On the bottom right put Song 9- again just fill the space with the song.
I have provided some photos to put into the 35 mm film. Please keep to the order. (some of these photos may change)
Photo1- 3598 (cut off)
Photo 2- 3599
Photo 3- 3545
Photo 4- Photo of Copper kites (example provided)
Photo 5- 3382 (cut off)
The background I'm in two minds over- if you have any ideas for the background that compliment page 6 that would be great. Again keep this simple as the opposing page is busy.
Page 8- Song 10 (linger near)
Photo of beach (provided image 3541)
Instamatic photo 422599 bottom left with photo 3447 inserted.
Song 10 lyrics in the sky of the picture maybe like the shape of a cloud or something else creative
Page 9- Song 11 (windswept) and 12 ( velvet static)
Song 12 lyrics should be superimposed onto the orange ice block image 31.
Song 11 lyrics could go all around the icy pole in a circular vortex style. Also I'm not sure whether to do a white background or use the ice cubes as the background image 4985063 what do you think?
Page 10
This will be a page of photos of the recording.
I would like 4 horizontal 35mm film strips if possible with 4 frames per line.
Starting right to left insert images.
Row 1: 5574,5636,5905,5521
Row 2: 5465,5200,5931,5048
Row 3: 7978,6140,3618,6091
Row 4: 5221,5373,5076,5810
Page 12: I was going to try to supply a picture but you may be able to create what I am after.
Its a photo of a wheelchair at the side of the ocean with a tequila sunrise drink on the ground next to the wheel or thereabouts with a cocktail umbrella in it. I will upload to pictures for imagery. If you can't pull it off that ok, I will have to try to mock up a photo myself. Photos of wheel chair are:
Page 11. The credits page.
1.Black background and white writing. Try to make it look like the credits that run at the end of a movie as this page is opposed to the 35mm picture. If in your opinion that doesn't work then just keep it black background white writing as per uploaded.
On the second uploaded page I have written what I want done in terms of credits for each song writer. Each heading of each song within the body of the booklet needs to have the credits for each songwriter for that particular song placed in parentheses and in much smaller font directly below each song name. This is a traditional way to do it as it will allow for more space on page 11.
Page 12: a photo to be provided- see Image 3970 copy- insert as page 12
Final: Spine of CD- White background, put the word ''quiet harbor'' (In the middle with orange font- same font as front cover) and put the word
''MARIGOLD HUSH'' (On the right side in black font-same as front cover) on the far left write''Tin Lantern'' in Black smaller font and understated.
MARIGOLD HUSH quiet harbor Tin Lantern
****I have now added photos to replace 21 and 22 in the 35mm photo collage page 10 of inside sleeve****

```html
<!DOCTYPE html>
<html lang="en">
<head>
<meta charset="utf-8">
<title>Booklet Page 2 – Lyrics</title>
<link href="https://fonts.googleapis.com/css2?family=Questrial&display=swap" rel="stylesheet">
<style>
  :root {
    --paper: #ffffff;
    --title-blue: #1570a6;
    --lyric-orange: #ee7a2c;
    --umbrella-light: #f9a650;
    --umbrella-dark: #e96a1c;
    --print-cream: #ece6d6;
    --tape: rgba(214, 190, 140, 0.78);
    --sea-light: #c9c2c4;
    --sea-dark: #2a2a30;
  }
  * { margin: 0; padding: 0; box-sizing: border-box; }
  html, body { width: 1200px; height: 1200px; overflow: hidden; background: var(--paper); }
  .page {
    position: relative;
    width: 1200px;
    height: 1200px;
    background: var(--paper);
    font-family: "Questrial", "Century Gothic", sans-serif;
    text-transform: uppercase;
  }
  .song-title {
    position: absolute;
    top: 48px;
    color: var(--title-blue);
    font-weight: 400;
    font-size: 43px;
    letter-spacing: 0.5px;
    white-space: nowrap;
    line-height: 1;
  }
  .song-title--left { right: 620px; text-align: right; }
  .song-title--right { left: 610px; }
  .song-title__sub { font-size: 33px; }
  .lyrics {
    position: absolute;
    top: 106px;
    color: var(--lyric-orange);
    white-space: nowrap;
    list-style: none;
  }
  .lyrics li { display: block; min-height: 1em; }
  .lyrics--left {
    right: 614px;
    text-align: right;
    font-size: 19.5px;
    line-height: 25.2px;
    letter-spacing: -0.2px;
  }
  .lyrics--right {
    top: 110px;
    left: 610px;
    font-size: 18.5px;
    line-height: 24px;
    letter-spacing: -0.2px;
  }
  .lyrics .gap { height: 25.2px; }
  .lyrics--right .gap { height: 24px; }
  .umbrella {
    position: absolute;
    left: 16px;
    top: 962px;
    width: 210px;
    height: 172px;
    border-radius: 50%;
    transform: rotate(-18deg);
    background: radial-gradient(circle at 55% 45%, var(--umbrella-light), var(--umbrella-dark) 75%);
  }
  .snapshot {
    position: absolute;
    left: 966px;
    top: 950px;
    width: 212px;
    height: 226px;
    transform: rotate(8deg);
    background: var(--print-cream);
    padding: 14px 14px 40px;
    box-shadow: 0 4px 10px rgba(0,0,0,0.18);
  }
  .snapshot__image {
    width: 100%;
    height: 100%;
    background: linear-gradient(180deg, var(--sea-light) 0%, #8d8790 40%, var(--sea-dark) 100%);
  }
  .snapshot__tape {
    position: absolute;
    width: 56px;
    height: 24px;
    background: var(--tape);
  }
  .snapshot__tape--tl { left: -18px; top: -6px; transform: rotate(-40deg); }
  .snapshot__tape--tr { right: -18px; top: -4px; transform: rotate(45deg); }
  .snapshot__tape--bl { left: -20px; bottom: 2px; transform: rotate(50deg); }
  .snapshot__tape--br { right: -18px; bottom: -2px; transform: rotate(-45deg); }
</style>
</head>
<body>
<main class="page">
  <h2 class="song-title song-title--left">Drifting Slowly</h2>
  <h2 class="song-title song-title--right">Far Away <span class="song-title__sub">(The Hidden Track)</span></h2>

  <ul class="lyrics lyrics--left">
    <li>Until the breeze comes back</li>
    <li>And leads me home, once more</li>
    <li>Oh, my tired eyes</li>
    <li>All the nights I lay awake</li>
    <li class="gap"></li>
    <li>Echoes, I knew are drifting</li>
    <li>Like the gulls circling over me</li>
    <li>Let it go, my quiet yesterdays</li>
    <li>Oh, how it aches to let it go</li>
    <li class="gap"></li>
    <li>Drifting slowly, maybe someday, I will find my home</li>
    <li>Drifting slowly, maybe someday, I will find my home</li>
    <li class="gap"></li>
    <li>I wish the warmth inside you stays</li>
    <li>When you learn the truth behind the words</li>
    <li>You won’t find me on the shore</li>
    <li>For the restless waves pull me on</li>
    <li class="gap"></li>
    <li>The stars follow, they follow me, onward</li>
    <li>My heart, the swell, rises softly</li>
    <li>Gentle echoes of the bay</li>
    <li>It isn’t right, nobody sees</li>
    <li class="gap"></li>
    <li>Drifting slowly, maybe someday, I will find my home</li>
    <li>Drifting slowly, maybe someday, I will find my home</li>
    <li class="gap"></li>
    <li>Until the breeze comes back</li>
    <li>And leads me home, once more</li>
    <li>Oh, my tired eyes</li>
    <li>Yeah, all the nights I lay awake</li>
    <li class="gap"></li>
    <li>Drifting slowly</li>
    <li>Maybe someday, I will find my home</li>
    <li>Drifting slowly</li>
    <li>Maybe someday, I will find my home</li>
    <li>Drifting slowly</li>
    <li>Maybe someday, I will find my home</li>
    <li>Drifting slowly</li>
    <li>Maybe someday, I will find my home</li>
  </ul>

  <ul class="lyrics lyrics--right">
    <li>I was only wandering</li>
    <li>Years ago, wandering to a shore</li>
    <li>Where I could rest my restless heart</li>
    <li class="gap"></li>
    <li>Nobody walked with me</li>
    <li>Seemed the sky was only drawn for me</li>
    <li>So how could love ever find me here</li>
    <li class="gap"></li>
    <li>That’s why I need a little gentle reminding</li>
    <li>Don’t you know I’d never leave you behind</li>
    <li>A light enough to guide me through</li>
    <li>Of love when it was brand new</li>
    <li class="gap"></li>
    <li>Far away the lanterns glow, calling me across the bay</li>
    <li>Far away, love will find a way</li>
    <li>Far away the lanterns glow, calling me across the bay</li>
    <li>Far away, love will find a way</li>
    <li class="gap"></li>
    <li>If we were together</li>
    <li>There’s a secret I’ll only share with you</li>
    <li>A quiet secret just for you</li>
    <li class="gap"></li>
    <li>That’s why I need a little gentle reminding</li>
    <li>Don’t you know I’d never leave you behind</li>
    <li>A light enough to guide me through</li>
    <li>Of love when it was brand new</li>
    <li class="gap"></li>
    <li>Far away the lanterns glow, calling me across the bay</li>
    <li>Far away, love will find a way</li>
    <li>Far away the lanterns glow, calling me across the bay</li>
    <li>Far away, love will find a way</li>
    <li class="gap"></li>
    <li>Far away they chase the stars</li>
    <li>All of this and more</li>
    <li>All I ever want is you right here</li>
    <li class="gap"></li>
    <li>Far away the lanterns glow,</li>
    <li>Calling me across the bay</li>
    <li>Far away, love will find a way</li>
    <li>Far away the lanterns glow,</li>
    <li>Calling me across the bay</li>
    <li>Far away, love will find a way</li>
  </ul>

  <div class="umbrella" role="img" aria-label="Orange paper cocktail umbrella resting on its side"></div>

  <div class="snapshot">
    <div class="snapshot__image" role="img" aria-label="Instant photo showing a sunrise over the ocean"></div>
    <span class="snapshot__tape snapshot__tape--tl"></span>
    <span class="snapshot__tape snapshot__tape--tr"></span>
    <span class="snapshot__tape snapshot__tape--bl"></span>
    <span class="snapshot__tape snapshot__tape--br"></span>
  </div>
</main>
</body>
</html>
```